A4 Block Hour Agreement Brochure

We need a new Block Hour Agreement Brochure created as our current one lacks design and is ugly. The current block hour agreement brochure has been attached "pixelharbor.pdf".

We are looking at a modern brochure and have attached "Vellamore Private Cloud Plans.pdf" as an example.

It doesnt have to be the exact same design, but it must be the "Vellamore blue" theme.

Target Market(s)

Information Technology

Colors
0054AA
0677BA
7BADD7
CADEEF
E8F1F8

```html
<!DOCTYPE html>
<html lang="en">
<head>
<meta charset="utf-8">
<title>Vellamore Technologies – Block Hour Agreement</title>
<link rel="stylesheet" href="https://fonts.googleapis.com/css2?family=Exo+2:ital,wght@1,700;1,800;1,900&family=Poppins:ital,wght@0,400;0,600;1,500&display=swap">
<style>
  :root {
    --navy: #1f2a7a;
    --deep: #15256b;
    --brand: #0054aa;
    --mid: #0677ba;
    --sky: #22a9e1;
    --soft: #7badd7;
    --pale: #cadeef;
    --mist: #e8f1f8;
    --text: #55585f;
    --rule: #c9cbd0;
    --cell: #e4e5e8;
    --stage: #ececec;
  }
  * { margin: 0; padding: 0; box-sizing: border-box; }
  html, body { width: 980px; height: 1200px; overflow: hidden; background: var(--stage); }
  .flyer {
    position: absolute; left: 66px; top: 0;
    width: 1061px; height: 1502px;
    transform: scale(0.799); transform-origin: 0 0;
    background: #fff; overflow: hidden;
    font-family: "Poppins", sans-serif;
  }
  .shapes { position: absolute; inset: 0; }
  .brand {
    position: absolute; left: 50px; top: 88px;
    display: flex; align-items: center; gap: 16px;
    font-family: "Poppins", sans-serif; font-weight: 600;
    color: var(--navy); font-size: 32px; letter-spacing: 3px; line-height: 1;
  }
  .brand-square { width: 28px; height: 28px; background: var(--brand); }
  .title {
    position: absolute; left: 46px; top: 262px;
    font-family: "Exo 2", sans-serif; font-style: italic; font-weight: 900;
    font-size: 72px; line-height: 58px; color: var(--navy); text-transform: uppercase;
  }
  .overview-heading {
    position: absolute; left: 48px; top: 470px;
    font-family: "Exo 2", sans-serif; font-style: italic; font-weight: 800;
    font-size: 44px; color: var(--navy);
  }
  .overview-body { position: absolute; left: 48px; top: 514px; }
  .overview-body p {
    font-size: 19px; line-height: 28.6px; color: var(--text);
    margin-bottom: 10px; white-space: nowrap;
  }
  .terms { position: absolute; left: 48px; top: 872px; list-style: none; }
  .terms li {
    position: relative; padding: 3px 0 3px 32px;
    font-style: italic; font-weight: 500; font-size: 18.5px; line-height: 21.5px;
    color: var(--navy); white-space: nowrap;
    border-bottom: 1.5px solid var(--rule);
  }
  .terms li:nth-child(1) { width: 708px; }
  .terms li:nth-child(2) { width: 680px; }
  .terms li:nth-child(3) { width: 652px; }
  .terms li:nth-child(4) { width: 600px; }
  .terms li:nth-child(5) { width: 572px; }
  .terms li:last-child { border-bottom: none; width: 520px; }
  .terms li::before {
    content: ""; position: absolute; left: 2px; top: 8px;
    width: 11px; height: 11px; background: var(--brand);
  }
  .network-art {
    position: absolute; left: 50px; top: 1145px; width: 310px; height: 232px;
    border-radius: 50%;
    background: radial-gradient(ellipse at center, var(--pale) 0%, var(--mist) 55%, rgba(255,255,255,0) 72%);
  }
  .types-heading {
    position: absolute; right: 48px; top: 990px; text-align: right;
    font-family: "Exo 2", sans-serif; font-style: italic; font-weight: 800;
    font-size: 48px; line-height: 50px; color: #fff;
  }
  .rates { position: absolute; left: 0; top: 1111px; width: 1061px; }
  .rate-row { position: relative; height: 43px; margin-bottom: 7px; font-weight: 600; font-size: 19px; }
  .rate-hours {
    position: absolute; left: 330px; width: 312px; height: 43px;
    background: linear-gradient(90deg, rgba(21,37,107,0) 0%, var(--deep) 60%, var(--deep) 100%);
    color: #fff; text-align: right; padding-right: 30px; line-height: 43px;
  }
  .rate-price {
    position: absolute; left: 648px; width: 164px; height: 43px;
    background: var(--cell); color: var(--navy); line-height: 43px; padding-left: 44px;
  }
  .rate-total {
    position: absolute; left: 820px; width: 241px; height: 43px;
    background: var(--sky); color: #fff; line-height: 43px; padding-left: 40px;
  }
  .contact {
    position: absolute; top: 1446px; height: 30px;
    display: flex; align-items: center; gap: 8px;
    font-size: 18px; color: var(--navy);
  }
  .contact-phone { left: 365px; }
  .contact-email { left: 632px; }
</style>
</head>
<body>
<main class="flyer">
  <svg class="shapes" viewBox="0 0 1061 1502" width="1061" height="1502" aria-hidden="true">
    <defs>
      <linearGradient id="bandGrad" x1="0" y1="0" x2="1" y2="1">
        <stop offset="0" stop-color="#1d2a86"/>
        <stop offset="0.55" stop-color="#0054aa"/>
        <stop offset="1" stop-color="#0677ba"/>
      </linearGradient>
      <linearGradient id="deepGrad" x1="0.7" y1="0" x2="0.2" y2="1">
        <stop offset="0" stop-color="#0d1f63"/>
        <stop offset="0.5" stop-color="#0f3c8c"/>
        <stop offset="1" stop-color="#0677ba"/>
      </linearGradient>
      <linearGradient id="photoGrad" x1="0" y1="0" x2="1" y2="1">
        <stop offset="0" stop-color="#f1f1f1"/>
        <stop offset="0.5" stop-color="#8e8e8e"/>
        <stop offset="1" stop-color="#3a3a3a"/>
      </linearGradient>
      <linearGradient id="cornerGrad" x1="0" y1="0" x2="1" y2="1">
        <stop offset="0" stop-color="#0054aa"/>
        <stop offset="1" stop-color="#0677ba"/>
      </linearGradient>
    </defs>
    <polygon points="200,0 320,0 365,47 245,47" fill="#1d3f9e"/>
    <polygon points="320,0 407,0 452,47 365,47" fill="#0677ba"/>
    <polygon points="560,0 1061,0 1061,741 480,160" fill="url(#photoGrad)" role="img" aria-label="Photo of two businessmen looking at a screen"/>
    <polygon points="362,160 480,160 1061,741 1061,859" fill="url(#bandGrad)"/>
    <polygon points="932,734 1061,862 1061,1502 165,1502" fill="url(#deepGrad)" role="img" aria-label="Blue glowing bokeh light background"/>
    <polygon points="0,1294 208,1502 0,1502" fill="url(#cornerGrad)"/>
    <polygon points="352,1416 1061,1416 1061,1502 266,1502" fill="#e6e7ea"/>
  </svg>

  <div class="brand"><span class="brand-square"></span>Vellamore Technologies</div>

  <h1 class="title">Block<br>Hour<br>Agreement</h1>

  <h2 class="overview-heading">Overview</h2>
  <div class="overview-body">
    <p>Vellamore Technologies offers the Block Time Service Agreement<br>at a discounted hourly rate for clients who need consistent support<br>throughout a period of time. A block time agreement lets you pre-pay<br>for services and call upon them as needed, this allows for easy accounting<br>and easy support.</p>
    <p>Our Block Time Service Agreement can be used for all non-project related work,<br>please ask your Vellamore representative for more details.</p>
    <p>Block hours are not covered under a Service Level Agreement (SLA) and are best<br>effort, while we endeavor to always provide prompt service to our customers in<br>some situations such as a service disruption, it may not always be possible to<br>attend straight away.</p>
  </div>

  <ul class="terms">
    <li>Block hours do not rollover</li>
    <li>There is no set usage per week.</li>
    <li>Project services cannot be used with block time.</li>
    <li>Time is billed in 0.5 hour increments with a minimum<br>of 1 hour for onsite callouts.</li>
    <li>Hours must be used within 12 months of purchase</li>
    <li>Hours must be used during standard business<br>hours 8:30am-5pm AWST. After hours is<br>charged at double time.</li>
  </ul>

  <div class="network-art" role="img" aria-label="Illustration of a globe connected by arrows to computers, phones and servers"></div>

  <h2 class="types-heading">Agreement<br>Types</h2>

  <div class="rates">
    <div class="rate-row"><span class="rate-hours">1</span><span class="rate-price">$270.00</span><span class="rate-total">$265.00</span></div>
    <div class="rate-row"><span class="rate-hours">10</span><span class="rate-price">$240.00</span><span class="rate-total">$2,400.00</span></div>
    <div class="rate-row"><span class="rate-hours">20</span><span class="rate-price">$225.00</span><span class="rate-total">$4,500.00</span></div>
    <div class="rate-row"><span class="rate-hours">35</span><span class="rate-price">$220.00</span><span class="rate-total">$7,700.00</span></div>
    <div class="rate-row"><span class="rate-hours">50</span><span class="rate-price">$210.00</span><span class="rate-total">$10,500.00</span></div>
  </div>

  <div class="contact contact-phone">
    <svg width="18" height="18" viewBox="0 0 24 24" aria-hidden="true"><path fill="#22a9e1" d="M6.6 10.8c1.4 2.8 3.8 5.1 6.6 6.6l2.2-2.2c.3-.3.7-.4 1-.2 1.1.4 2.3.6 3.6.6.6 0 1 .4 1 1V20c0 .6-.4 1-1 1C10.6 21 3 13.4 3 4c0-.6.4-1 1-1h3.5c.6 0 1 .4 1 1 0 1.3.2 2.5.6 3.6.1.3 0 .7-.2 1z"/></svg>
    <span>08 5550 1234</span>
  </div>
  <div class="contact contact-email">
    <svg width="18" height="14" viewBox="0 0 24 18" aria-hidden="true"><rect x="0" y="0" width="24" height="18" rx="2" fill="#22a9e1"/><path d="M1 2l11 8 11-8" fill="none" stroke="#fff" stroke-width="2"/></svg>
    <span>sales@vellamoretech.com.au</span>
  </div>
</main>
</body>
</html>
```